I want a business card design. the company is an infrastructure development company.

Target Market(s)

Government
real estate investors
real estate clients

Industry/Entity Type

Business

```html
<!DOCTYPE html>
<html lang="en">
<head>
<meta charset="utf-8">
<title>Crestline Builders – Business Card</title>
<link rel="stylesheet" href="https://fonts.googleapis.com/css2?family=Open+Sans:wght@400;600&family=Roboto+Condensed:wght@300&display=swap">
<style>
  :root {
    --page-bg: #8e8f8f;
    --card-bg: #ffffff;
    --brand-red: #e2363f;
    --brand-blue: #2db7dc;
    --name-blue: #3bb0e0;
    --ink-dark: #1f1f1f;
    --ink-grey: #8a8a8a;
  }
  * { box-sizing: border-box; margin: 0; padding: 0; }
  html, body {
    width: 1200px;
    height: 1000px;
    overflow: hidden;
    background: var(--page-bg);
  }
  .card {
    position: absolute;
    left: 100px;
    top: 210px;
    width: 1000px;
    height: 580px;
    background: var(--card-bg);
    box-shadow: 0 6px 24px rgba(0,0,0,0.25);
    font-family: "Open Sans", Arial, sans-serif;
    overflow: hidden;
  }
  .brand {
    position: absolute;
    left: 70px;
    top: 62px;
    display: flex;
    align-items: center;
    gap: 14px;
  }
  .brand-mark {
    width: 34px;
    height: 34px;
    background: var(--brand-red);
  }
  .brand-name {
    font-weight: 600;
    font-size: 30px;
    letter-spacing: 1px;
    color: var(--brand-red);
    text-transform: uppercase;
  }
  .accent-area {
    position: absolute;
    left: 0;
    top: 330px;
    width: 300px;
    height: 200px;
    background: linear-gradient(135deg, rgba(45,183,220,0.35), rgba(226,54,63,0.35));
  }
  .details {
    position: absolute;
    left: 560px;
    top: 160px;
    width: 420px;
  }
  .person-name {
    font-family: "Roboto Condensed", Arial, sans-serif;
    font-weight: 300;
    font-size: 40px;
    line-height: 1.3;
    color: var(--name-blue);
    margin-bottom: 20px;
  }
  .direct-lines {
    font-size: 19px;
    line-height: 1.4;
    color: var(--ink-dark);
    margin-bottom: 22px;
  }
  .office-address,
  .office-lines {
    font-size: 18px;
    line-height: 1.4;
    color: var(--ink-grey);
    margin-bottom: 20px;
  }
  .web-contacts { list-style: none; }
  .web-contacts li {
    display: flex;
    align-items: center;
    gap: 12px;
    font-size: 18px;
    line-height: 1.6;
    color: var(--ink-grey);
  }
  .web-icon { flex: none; }
</style>
</head>
<body>
  <main class="card">
    <div class="brand">
      <span class="brand-mark"></span>
      <span class="brand-name">Crestline Builders</span>
    </div>

    <div class="accent-area" role="img" aria-label="Decorative red and blue accent area"></div>

    <section class="details">
      <h1 class="person-name">Tobi Adeyemi, MD.</h1>
      <p class="direct-lines">
        +234 8010000101<br>
        +234 7010000202<br>
        tobi@crestlinebuilders.com
      </p>
      <p class="office-address">
        12 Harbour Close, Off Palm Grove Road,<br>
        Eastgate City, Nigeria
      </p>
      <p class="office-lines">
        +234 10000303<br>
        +234 7010000404
      </p>
      <ul class="web-contacts">
        <li>
          <svg class="web-icon" width="18" height="18" viewBox="0 0 18 18" aria-hidden="true">
            <circle cx="9" cy="9" r="9" fill="var(--brand-red)"/>
            <rect x="4" y="5.5" width="10" height="7" fill="none" stroke="#fff" stroke-width="1.2"/>
            <polyline points="4,5.5 9,9.5 14,5.5" fill="none" stroke="#fff" stroke-width="1.2"/>
          </svg>
          info@crestlinebuilders.com
        </li>
        <li>
          <svg class="web-icon" width="18" height="18" viewBox="0 0 18 18" aria-hidden="true">
            <circle cx="9" cy="9" r="9" fill="var(--brand-red)"/>
            <circle cx="9" cy="9" r="5" fill="none" stroke="#fff" stroke-width="1.1"/>
            <line x1="4" y1="9" x2="14" y2="9" stroke="#fff" stroke-width="1.1"/>
            <ellipse cx="9" cy="9" rx="2.2" ry="5" fill="none" stroke="#fff" stroke-width="1.1"/>
          </svg>
          www.crestlinebuilders.com
        </li>
      </ul>
    </section>
  </main>
</body>
</html>
```